Lumara Health & Wellness Business Card Design

We would like to create business cards matching with our new logo design. The card should be professional looking but still have a playful side and something that would be eye catching. We are planing to open a luxury medical spa and looking to create a design based on this new logo. We are looking for a design that shows off luxury but not be gold in color. Also, while we are a more female oriented medical center we do have men that come in for our services and it should be be too feminine.

Target Market(s)

Health & Wellness. Medical patients. Luxury spa

Industry/Entity Type

Health And Wellness

Contact Information for Business Card

It should have the logo design in the front of card and back of card should have our contact information. Our current colors are peach/ coral, teal, and gray. We are looking for a modern looking design.

Font styles to use
Script

Colors
32a6d6
e667a6
86cfc6
fece3e

Requirements
Must have
• It should have our logo design. We would prefer to have a more modern look to the card.
Nice to have
• Eye-Catching Design on the personable side but still classy.
Should not have
• At this point we are looking for the best design. It should not have color purple.

```html
<!DOCTYPE html>
<html lang="en">
<head>
<meta charset="utf-8">
<title>Lumara Health &amp; Wellness – Business Card</title>
<link rel="stylesheet" href="https://fonts.googleapis.com/css2?family=Playfair+Display:ital,wght@0,400;1,400&display=swap">
<style>
  :root {
    --backdrop: #2f2f2f;
    --card-white: #ffffff;
    --band-pink: #f77297;
    --brand-teal: #02978e;
    --ink-light: #f3f3f3;
    --ink-pale: #e2e2e2;
  }
  * { margin: 0; padding: 0; box-sizing: border-box; }
  html, body {
    width: 1200px;
    height: 952px;
    overflow: hidden;
    background: var(--backdrop);
  }
  .canvas {
    position: relative;
    width: 1200px;
    height: 952px;
  }
  .card {
    position: absolute;
    left: 346px;
    width: 520px;
    height: 316px;
    border-radius: 24px;
    overflow: hidden;
  }
  .card--front {
    top: 148px;
    background: var(--card-white);
  }
  .card--back {
    top: 490px;
    background: var(--brand-teal);
  }
  .front-band {
    position: absolute;
    left: 0;
    top: 98px;
    width: 520px;
    height: 126px;
  }
  .front-band polygon { fill: var(--band-pink); }
  .contact-list {
    position: absolute;
    left: 40px;
    top: 114px;
    list-style: none;
    font-family: "Playfair Display", serif;
    font-style: italic;
    font-size: 15px;
    line-height: 28px;
    color: var(--ink-light);
    white-space: nowrap;
  }
  .brand-name {
    position: absolute;
    font-family: "Playfair Display", serif;
    font-weight: 400;
    white-space: nowrap;
    display: flex;
    align-items: center;
    gap: 7px;
  }
  .brand-name--front {
    left: 262px;
    top: 150px;
    font-size: 16px;
    color: var(--brand-teal);
  }
  .brand-name--back {
    left: 50%;
    top: 50%;
    transform: translate(-50%, -50%);
    font-size: 22px;
    color: var(--ink-pale);
  }
  .brand-dot {
    width: 9px;
    height: 9px;
    border-radius: 50%;
    background: currentColor;
    flex: none;
  }
</style>
</head>
<body>
<main class="canvas">
  <section class="card card--front" aria-label="Business card front">
    <svg class="front-band" viewBox="0 0 520 126" aria-hidden="true">
      <polygon points="0,0 350,0 250,126 0,126"/>
    </svg>
    <ul class="contact-list">
      <li>www.lumarawellness.com</li>
      <li>info@lumarawellness.com</li>
      <li>022 555 610 4821</li>
    </ul>
    <p class="brand-name brand-name--front"><span class="brand-dot"></span>Lumara Health &amp; Wellness</p>
  </section>

  <section class="card card--back" aria-label="Business card back">
    <p class="brand-name brand-name--back"><span class="brand-dot"></span>Lumara Health &amp; Wellness</p>
  </section>
</main>
</body>
</html>
```